Law Firm Needs Brochure Redesign Using New Logo

We are a personal injury law firm that does auto injuries and other personal injury cases. We want a new brochure that has our updated logo and information. Instead of gold and black, we want more navy, as matches the new logo. The Auto Liability portion should read: "(required by the state of Arizona in the amounts of $25,000 per person / $50,000 per accident, but a higher amount may be best )." The other information can remain the same. We'd like the brochure to keep the same professional tone as the previous brochure.
Our website is https://www.marbrenlegal.com/.

```html
<!DOCTYPE html>
<html lang="en">
<head>
<meta charset="utf-8">
<title>Marbren Legal – Car Accident Brochure</title>
<link href="https://fonts.googleapis.com/css2?family=Rubik:wght@300;400;500;700&family=Roboto:wght@300;400&display=swap" rel="stylesheet">
<style>
  :root{
    --navy:#0e2447;
    --navy-deep:#0a1c3a;
    --slate:#6d7f97;
    --slate-light:#c8d2e0;
    --ink:#1d2433;
    --paper:#ffffff;
    --backdrop:#e7e5e1;
    --faint:#eef0f4;
  }
  *{box-sizing:border-box;margin:0;padding:0}
  html,body{width:1200px;height:1200px;overflow:hidden}
  body{background:var(--backdrop);font-family:'Rubik',sans-serif;color:var(--ink);position:relative}

  .sheet{position:absolute;left:235px;width:730px;height:565px;display:grid;grid-template-columns:1fr 1fr 1fr;box-shadow:0 4px 14px rgba(0,0,0,.25)}
  .sheet--outside{top:25px}
  .sheet--inside{top:610px}
  .panel{position:relative;overflow:hidden}

  /* ---------- Outside: stats panel ---------- */
  .stats{background:var(--navy);color:#fff;font-family:'Roboto',sans-serif;text-align:center}
  .stats__photo{position:absolute;inset:0;background:linear-gradient(180deg,#0f2548 0%,#163462 45%,#2a4d80 70%,#14305a 100%)}
  .stat{position:absolute;left:0;right:0}
  .stat__over{font-size:11px;font-weight:300;letter-spacing:.3px}
  .stat__number{font-size:41px;font-weight:400;line-height:1;margin-top:2px;letter-spacing:-.5px}
  .stat__caption{font-size:11.5px;font-weight:300;line-height:14px;margin-top:1px}
  .stat--crashes{top:100px}
  .stat--fatal{top:235px}
  .stat--fatal .stat__number{font-size:40px}
  .stats__pledge{position:absolute;top:400px;left:30px;right:30px;font-family:'Rubik',sans-serif;font-weight:300;font-size:10.2px;line-height:13.6px}

  /* ---------- Outside: mailer panel ---------- */
  .mailer{background:var(--paper)}
  .mailer__mark{position:absolute;left:96px;top:150px;writing-mode:vertical-rl;transform:rotate(180deg);font-weight:700;font-size:24px;color:var(--faint);letter-spacing:1px}
  .mailer__return{position:absolute;left:16px;bottom:16px;writing-mode:vertical-rl;transform:rotate(180deg);display:flex;gap:6px;align-items:flex-start}
  .mailer__name{font-weight:700;font-size:13px;color:var(--navy);letter-spacing:.5px}
  .mailer__address{font-family:'Roboto',sans-serif;font-weight:300;font-size:8.6px;line-height:14px;color:var(--ink)}

  /* ---------- Outside: cover panel ---------- */
  .cover{background:var(--navy);display:flex;flex-direction:column}
  .cover__brand{height:94px;background:var(--paper);display:flex;align-items:center;justify-content:center;gap:8px}
  .cover__brand-dot{width:14px;height:14px;border-radius:50%;background:var(--navy)}
  .cover__brand-name{font-weight:700;font-size:19px;color:var(--navy);letter-spacing:1.2px}
  .cover__photo{height:338px;background:radial-gradient(circle at 75% 25%,#c69a62 0%,#6d563f 30%,#2f2f33 60%,#1d1e24 100%)}
  .cover__headline{height:97px;color:#fff;text-align:center;padding-top:9px}
  .cover__title{font-weight:500;font-size:17px;line-height:21px}
  .cover__sub{font-family:'Roboto',sans-serif;font-weight:300;font-size:12.6px;line-height:15.5px;margin-top:4px}
  .cover__url{height:19px;background:var(--slate);color:var(--navy);font-weight:700;font-size:10px;letter-spacing:2px;display:flex;align-items:center;justify-content:center}
  .cover__foot{flex:1}

  /* ---------- Inside: tips panel ---------- */
  .tips{background:var(--navy);color:var(--slate-light)}
  .tips__title{position:absolute;left:26px;top:24px;font-weight:700;font-size:12px;letter-spacing:.2px}
  .tips__rail{position:absolute;left:42px;top:70px;height:450px;border-left:1px dotted var(--slate-light)}
  .tip__num{position:absolute;left:26px;width:32px;height:32px;border-radius:50%;background:var(--slate-light);border:2.5px solid #fff;box-shadow:0 0 0 1.5px var(--slate);display:flex;align-items:center;justify-content:center;font-weight:700;font-size:17px;color:var(--navy)}
  .tip__text{position:absolute;left:68px;right:24px;font-weight:300;font-size:8.8px;line-height:11.6px;text-align:justify;color:#c4cedb}
  .tip__text strong{font-weight:400;color:#e4e9f0}

  /* ---------- Inside: coverage panel ---------- */
  .coverage{background:var(--paper)}
  .coverage__photo{height:285px;background:linear-gradient(160deg,#3d4658 0%,#262d3c 45%,#1b2130 100%)}
  .band{background:var(--slate);color:#fff;font-weight:700;font-size:12px;display:flex;align-items:center;padding-left:26px;letter-spacing:.2px}
  .coverage .band{height:28px}
  .coverage__body{padding:8px 26px 0 26px}
  .coverage__intro{font-weight:500;font-size:9px;line-height:11.6px;color:var(--navy);text-align:justify}
  .coverage__list{list-style:none;margin-top:7px;border-left:1px dotted #9aa6b8;margin-left:3px}
  .coverage__item{position:relative;padding-left:10px;font-weight:300;font-size:8.8px;line-height:11.6px;text-align:justify;margin-bottom:6px;color:var(--ink)}
  .coverage__item strong{font-weight:500;color:var(--navy)}
  .coverage__tick{position:absolute;left:-4px;top:2px;width:7px;height:7px}

  /* ---------- Inside: safety + contact panel ---------- */
  .safety{background:var(--paper);display:flex;flex-direction:column}
  .safety__gap{height:16px}
  .safety .band{height:27px}
  .safety__text{padding:4px 26px 0 27px;font-weight:300;font-size:8.8px;line-height:11.6px;text-align:justify;color:var(--ink)}
  .safety__text strong{font-weight:500}
  .safety__text--buckle{height:46px}
  .safety__text--text{height:67px;padding-top:7px}
  .safety__text p+p{margin-top:5px}
  .contact{height:130px;background:var(--navy);color:#fff;padding:12px 20px 0 27px}
  .contact__title{font-weight:700;font-size:12px;color:var(--slate-light);margin-bottom:6px}
  .contact__row{display:flex;gap:6px;font-size:10px;line-height:12.8px;margin-bottom:4px}
  .contact__icon{flex:none;width:12px;height:12px;margin-top:1px}
  .safety__photo{flex:1;background:linear-gradient(135deg,#8a8f95 0%,#c9c4bc 40%,#6f6a66 75%,#2e2f33 100%)}
</style>
</head>
<body>

<!-- Outside spread -->
<section class="sheet sheet--outside">
  <div class="panel stats">
    <div class="stats__photo" role="img" aria-label="Photo of a long highway stretching through a forest, tinted navy"></div>
    <div class="stat stat--crashes">
      <div class="stat__over">OVER</div>
      <div class="stat__number">107,000</div>
      <div class="stat__caption">crashes will happen in the state of<br>Arizona this year.</div>
    </div>
    <div class="stat stat--fatal">
      <div class="stat__over">OVER</div>
      <div class="stat__number">700</div>
      <div class="stat__caption">of them will result in fatalities.</div>
    </div>
    <p class="stats__pledge">If we don't win, you don't pay attorney fees. That seems fair to us. Know what's happening with your case, get the answers to your questions and work on getting better with the confidence that you've got an excellent group of people working for you.</p>
  </div>

  <div class="panel mailer">
    <div class="mailer__mark" aria-hidden="true">MARBREN LEGAL</div>
    <div class="mailer__return">
      <span class="mailer__name">MARBREN LEGAL</span>
      <span class="mailer__address">4870 N. 16th Street Suite B310<br>Phoenix AZ 85016</span>
    </div>
  </div>

  <div class="panel cover">
    <div class="cover__brand">
      <span class="cover__brand-dot"></span>
      <span class="cover__brand-name">MARBREN LEGAL</span>
    </div>
    <div class="cover__photo" role="img" aria-label="Photo of a lawyer in a dark suit holding a glowing white car icon above his open hand"></div>
    <div class="cover__headline">
      <h1 class="cover__title">Protect your family in<br>case of a car accident</h1>
      <p class="cover__sub">A little knowledge and preparation<br>go a long way</p>
    </div>
    <div class="cover__url">www.marbrenlegal.com</div>
    <div class="cover__foot"></div>
  </div>
</section>

<!-- Inside spread -->
<section class="sheet sheet--inside">
  <div class="panel tips">
    <h2 class="tips__title">TOP 10 TIPS TO AVOID A CRASH</h2>
    <div class="tips__rail"></div>

    <div class="tip__num" style="top:45px">1</div>
    <p class="tip__text" style="top:45px">Anyone making a left turn must wait for all oncoming traffic to clear before proceeding. <strong>Yes, even if the light has turned yellow. Wait to be sure that all traffic has stopped.</strong></p>

    <div class="tip__num" style="top:114px">2</div>
    <p class="tip__text" style="top:113px">When your light turns green, <strong>check to be sure that no vehicles are entering the intersection late.</strong></p>

    <div class="tip__num" style="top:165px">3</div>
    <p class="tip__text" style="top:159px">Allow plenty of room between you and the car in front of you. <strong>Traffic can stop in an instant, even if you can't see anything ahead.</strong></p>

    <div class="tip__num" style="top:222px">4</div>
    <p class="tip__text" style="top:219px">Avoid being distracted. <strong>Teenagers are especially susceptible to losing focus if there are too many friends in the car.</strong></p>

    <div class="tip__num" style="top:283px">5</div>
    <p class="tip__text" style="top:276px">Keep the volume of your radio down and never wear headphones. <strong>Cars are very soundproof these days, but you need to be able to hear an ambulance or police siren.</strong></p>

    <div class="tip__num" style="top:342px">6</div>
    <p class="tip__text" style="top:346px">Be especially careful on the weekends and early morning hours.</p>

    <div class="tip__num" style="top:400px">7</div>
    <p class="tip__text" style="top:387px">Don't speed. <strong>Speed is a factor in most crashes. Street lights are timed and the freeway has traffic. It's likely you won't get there much faster even if you do speed.</strong></p>

    <div class="tip__num" style="top:457px">8</div>
    <p class="tip__text" style="top:457px">Don't drink and drive. <strong>Many cab companies offer a free service to get you home safe.</strong></p>

    <div class="tip__num" style="top:508px">9</div>
    <p class="tip__text" style="top:508px">Use your turn signals. <strong>This gives an early warning to vehicles you may not be able to see.</strong></p>
  </div>

  <div class="panel coverage">
    <div class="coverage__photo" role="img" aria-label="Photo of a man in a suit cupping his hands around a glowing blue shield with a car icon"></div>
    <h2 class="band">HAVE THE RIGHT COVERAGE</h2>
    <div class="coverage__body">
      <p class="coverage__intro">Many people don't know about the different kinds of insurance available. In addition to health insurance, we suggest:</p>
      <ul class="coverage__list">
        <li class="coverage__item"><svg class="coverage__tick" viewBox="0 0 10 10"><circle cx="5" cy="5" r="5" fill="#0e2447"/><path d="M2.6 5.2l1.6 1.6 3.2-3.4" stroke="#fff" stroke-width="1.4" fill="none"/></svg><strong>Auto Liability</strong> (required by the state of Arizona in the amounts of $25,000 per person / $50,000 per accident, but a higher amount may be best ).</li>
        <li class="coverage__item"><svg class="coverage__tick" viewBox="0 0 10 10"><circle cx="5" cy="5" r="5" fill="#0e2447"/><path d="M2.6 5.2l1.6 1.6 3.2-3.4" stroke="#fff" stroke-width="1.4" fill="none"/></svg><strong>Uninsured or Underinsured Motorist Coverage.</strong> This protects YOU when the other driver doesn't have insurance or not enough.</li>
        <li class="coverage__item"><svg class="coverage__tick" viewBox="0 0 10 10"><circle cx="5" cy="5" r="5" fill="#0e2447"/><path d="M2.6 5.2l1.6 1.6 3.2-3.4" stroke="#fff" stroke-width="1.4" fill="none"/></svg><strong>Medical Payments Coverage.</strong> Up to $5,000 in coverage will be paid out to you no matter who is at fault in an accident and does not need to be reimbursed.</li>
        <li class="coverage__item"><svg class="coverage__tick" viewBox="0 0 10 10"><circle cx="5" cy="5" r="5" fill="#0e2447"/><path d="M2.6 5.2l1.6 1.6 3.2-3.4" stroke="#fff" stroke-width="1.4" fill="none"/></svg><strong>Homeowners / Renters Insurance.</strong> Protects you in case of injuries on your property as well as damage to your home from covered events.</li>
      </ul>
    </div>
  </div>

  <div class="panel safety">
    <div class="safety__gap"></div>
    <h2 class="band">MODEL SAFE BEHAVIOR</h2>
    <div class="safety__text safety__text--buckle">
      <p><strong>Always buckle up.</strong> Always put your children in car seats/boosters that are rated for their height and weight.</p>
    </div>
    <h2 class="band">NEVER TEXT WHILE DRIVING</h2>
    <div class="safety__text safety__text--text">
      <p>Studies have shown that texting while driving is as dangerous as driving intoxicated.</p>
      <p><strong>Show your children that no text is more important than your safety. It can wait.</strong></p>
    </div>
    <div class="contact">
      <h2 class="contact__title">CONTACT US</h2>
      <div class="contact__row">
        <svg class="contact__icon" viewBox="0 0 12 12"><circle cx="6" cy="6" r="5.4" fill="none" stroke="#c8d2e0" stroke-width=".8"/><path d="M6 2.8a2 2 0 0 1 2 2c0 1.5-2 3.8-2 3.8s-2-2.3-2-3.8a2 2 0 0 1 2-2z" fill="none" stroke="#c8d2e0" stroke-width=".8"/></svg>
        <span>Marbren Legal Group<br>4870 N. 16th Street Suite B310<br>Phoenix AZ 85016</span>
      </div>
      <div class="contact__row">
        <svg class="contact__icon" viewBox="0 0 12 12"><circle cx="6" cy="6" r="5.4" fill="none" stroke="#c8d2e0" stroke-width=".8"/><path d="M4 3.2l1 1.3-.6.8a4 4 0 0 0 2.3 2.3l.8-.6 1.3 1-.6 1c-2.4-.2-4.6-2.4-4.8-4.8z" fill="#c8d2e0"/></svg>
        <span>602.555.0148</span>
      </div>
      <div class="contact__row">
        <svg class="contact__icon" viewBox="0 0 12 12"><circle cx="6" cy="6" r="5.4" fill="none" stroke="#c8d2e0" stroke-width=".8"/><rect x="3.2" y="4" width="5.6" height="4" fill="none" stroke="#c8d2e0" stroke-width=".7"/><path d="M3.2 4l2.8 2.2L8.8 4" fill="none" stroke="#c8d2e0" stroke-width=".7"/></svg>
        <span>info@MarbrenLegal.com</span>
      </div>
      <div class="contact__row">
        <svg class="contact__icon" viewBox="0 0 12 12"><circle cx="6" cy="6" r="5.4" fill="none" stroke="#c8d2e0" stroke-width=".8"/><circle cx="6" cy="6" r="2.9" fill="none" stroke="#c8d2e0" stroke-width=".6"/><path d="M3.1 6h5.8M6 3.1c-1.4 1.6-1.4 4.2 0 5.8M6 3.1c1.4 1.6 1.4 4.2 0 5.8" fill="none" stroke="#c8d2e0" stroke-width=".6"/></svg>
        <span>MarbrenLegal.com</span>
      </div>
    </div>
    <div class="safety__photo" role="img" aria-label="Photo of a pregnant woman fastening her seat belt in the driver's seat of a car"></div>
  </div>
</section>

</body>
</html>
```